LABEL DESIGN NEEDED FOR Mabel Fenwick Cookies

I am starting a Cookie Company with my daughter Mabel that will begin by making chocolate chip cookies.
These labels will go on a 2.5 by 2x6 clear cellophane bag that we will use to give out samples of our cookies to others to introduce our new- company to them.
I want the label to be 2X3 for both the front and the back.
These labels are for a cookie business starting out by making chocolate chip cookies. We will start out using clear cellophane bags with gold twist ties.
The size of the bags we will be using at first are 2.5x2x6 and 3.5x2x7.5.
Again, the clear cellophane bags will contain chocolate chip cookies that are round and weigh 1.5 oz. each.
On the front of the label I want it to have my logo which says Mabel Fenwick Cookies (see attached) with the name of the cookie (Chocolate Chip) and the weight (3oz.)
On the back of the label I would like the following:
Ingredients: All-purpose Flour, Semisweet Chocolate Chips, Granulated Sugar, Light Brown Sugar, Butter, Egg yolk, Light Corn Syrup, Milk, Vanilla Extract, Baking Soda, Salt
We also need it to say:
These products were manufactured in a facility that processes nuts and other known allergens. i.e. Milk, Eggs, Wheat, Soy
and it needs to have my address:
Larkhaven, Maine 11893
I have attached three things which will help the artist:
1.Our company logo (Mabel Fenwick Cookies)
2.A front and back label of a packaging from a cookie company that I really liked and thought was very cute. This should give the artist a start in terms of what direction to head in.
Thank you so much for all your help and just let me know what I need to do next.

```html
<!DOCTYPE html>
<html lang="en">
<head>
<meta charset="UTF-8">
<title>Mabel Fenwick Cookies – Back Label</title>
<link rel="stylesheet" href="https://fonts.googleapis.com/css2?family=Roboto:ital,wght@0,300;0,700;1,300&display=swap">
<style>
  :root {
    --label-brown: #6e4a2f;
    --cookie-tan: #b98a68;
    --cookie-rim: #4b4a49;
    --text-white: #ffffff;
  }
  html, body {
    margin: 0;
    padding: 0;
    width: 1200px;
    height: 800px;
    overflow: hidden;
    background: var(--label-brown);
  }
  .label-back {
    position: relative;
    width: 1200px;
    height: 800px;
    overflow: hidden;
    background: var(--label-brown);
    font-family: "Roboto", Arial, sans-serif;
    color: var(--text-white);
  }
  .cookie-art {
    position: absolute;
    inset: 0;
    width: 1200px;
    height: 800px;
  }
  .ingredients {
    position: absolute;
    left: 59px;
    top: 128px;
    width: 1085px;
    margin: 0;
    font-weight: 700;
    font-size: 41px;
    line-height: 53.5px;
    text-align: justify;
  }
  .allergen-note {
    position: absolute;
    left: 59px;
    top: 413px;
    width: 499px;
    margin: 0;
    font-weight: 300;
    font-style: italic;
    font-size: 40px;
    line-height: 54px;
    text-align: justify;
  }
  .address {
    position: absolute;
    left: 683px;
    top: 424px;
    display: flex;
    align-items: flex-start;
    gap: 29px;
    font-weight: 300;
    font-size: 44px;
    line-height: 55px;
  }
  .address-pin {
    width: 37px;
    height: 50px;
    margin-top: 9px;
    flex: none;
  }
  .address-text {
    margin: 0;
    white-space: nowrap;
  }
</style>
</head>
<body>
  <main class="label-back">
    <svg class="cookie-art" viewBox="0 0 1200 800" role="img" aria-label="Illustrated chocolate chip cookies with bites taken out, scattered around the label">
      <g fill="var(--cookie-tan)" stroke="var(--cookie-rim)" stroke-width="12">
        <circle cx="170" cy="305" r="285"/>
        <circle cx="1095" cy="128" r="172"/>
        <circle cx="880" cy="565" r="160"/>
        <circle cx="305" cy="725" r="108"/>
      </g>
    </svg>

    <p class="ingredients">Ingredients: All-purpose Flour, Semisweet Chocolate Chips, Granulated Sugar, Light Brown Sugar, Butter, Egg yolk, Light Corn Syrup, Milk, Vanilla Extract, Baking Soda, Salt</p>

    <p class="allergen-note">These products were manufactured in a facility that processes nuts and other known allergens. i.e. Milk, Eggs, Wheat, Soy.</p>

    <div class="address">
      <svg class="address-pin" viewBox="0 0 24 34" aria-hidden="true">
        <path fill="var(--text-white)" fill-rule="evenodd" d="M12 0C5.4 0 0 5.2 0 11.7 0 20.5 12 34 12 34s12-13.5 12-22.3C24 5.2 18.6 0 12 0zm0 16.5a4.8 4.8 0 1 1 0-9.6 4.8 4.8 0 0 1 0 9.6z"/>
      </svg>
      <p class="address-text">Larkhaven, Maine<br>11893</p>
    </div>
  </main>
</body>
</html>
```